Skin Care Online Ad - GIF or static

Odette Varga, an online seller of skin care products, wants to showcase our Eye Contour Serum and Collagen Eye Pads to potential customers on Chatterloop. Designer has 100% creative liberty. Designers may submit either a static ad or a GIF, we prefer a GIF. We want both web based formats and mobile formats to be delivered.

You can see our website at https://odettevarga.example
You can see our Eye Contour at https://odettevarga.example/eye-contour-revitalizing-serum
You can see our Collagen Eye Pads at https://odettevarga.example/hydrating-collagen-eye-pads-5-pack/

Both products are targeted at women ages 40-65 and are to help with the area under the eye to reduce puffiness and improve overall look.

```html
<!DOCTYPE html>
<html lang="en">
<head>
<meta charset="utf-8">
<title>Odette Varga – Reduce Puffiness &amp; Improve Overall Look</title>
<link rel="stylesheet" href="https://fonts.googleapis.com/css2?family=DM+Sans:wght@300;400;700&display=swap">
<style>
  :root {
    --paper: #ebebea;
    --magenta: #d1298f;
    --plum: #6e2a7c;
    --brand-grey: #5b5b5b;
    --sprig-tone: rgba(255, 255, 255, 0.16);
    --sprig-tone-on-paper: rgba(209, 41, 143, 0.10);
  }
  * { margin: 0; padding: 0; box-sizing: border-box; }
  html, body {
    width: 1200px;
    height: 1200px;
    overflow: hidden;
    background: var(--paper);
  }
  .ad {
    position: relative;
    width: 1200px;
    height: 1200px;
    overflow: hidden;
    background: var(--paper);
    font-family: "DM Sans", Arial, sans-serif;
  }
  .accent-disc {
    position: absolute;
    inset: 0;
  }
  .sprig {
    position: absolute;
    border-radius: 40% 60% 55% 45%;
  }
  .sprig--top {
    left: 860px; top: 0;
    width: 340px; height: 450px;
    background: linear-gradient(200deg, var(--sprig-tone), transparent 80%);
  }
  .sprig--bottom-right {
    left: 960px; top: 810px;
    width: 240px; height: 390px;
    background: linear-gradient(20deg, var(--sprig-tone), transparent 80%);
  }
  .sprig--bottom-center {
    left: 460px; top: 920px;
    width: 200px; height: 280px;
    background: linear-gradient(10deg, var(--sprig-tone-on-paper), transparent 85%);
  }
  .headline {
    position: absolute;
    left: 33px;
    top: 0;
    color: var(--magenta);
  }
  .headline span {
    position: absolute;
    left: 0;
    white-space: nowrap;
    line-height: 1;
    font-size: 100px;
    letter-spacing: -1px;
  }
  .headline .verb { font-weight: 700; }
  .headline .object { font-weight: 300; }
  .headline .line-1 { top: 222px; }
  .headline .line-2 { top: 310px; }
  .headline .amp {
    top: 460px;
    font-weight: 400;
    color: var(--plum);
    font-size: 92px;
  }
  .headline .line-3 { top: 595px; }
  .headline .line-4 { top: 688px; }
  .headline .line-5 { top: 778px; }
  .brand {
    position: absolute;
    left: 35px;
    top: 1092px;
    color: var(--brand-grey);
  }
  .brand-name {
    font-size: 46px;
    font-weight: 400;
    line-height: 1;
    letter-spacing: 0.5px;
  }
  .brand-tagline {
    margin-top: 6px;
    font-size: 27px;
    font-weight: 400;
    letter-spacing: 5.6px;
    line-height: 1;
  }
</style>
</head>
<body>
  <main class="ad">
    <svg class="accent-disc" width="1200" height="1200" viewBox="0 0 1200 1200" aria-hidden="true">
      <ellipse cx="1222" cy="600" rx="689" ry="1000" fill="var(--magenta)"/>
    </svg>

    <div class="sprig sprig--top" role="img" aria-label="Line-drawn leafy sprig decoration"></div>
    <div class="sprig sprig--bottom-right" role="img" aria-label="Line-drawn leafy sprig decoration"></div>
    <div class="sprig sprig--bottom-center" role="img" aria-label="Line-drawn leafy sprig decoration"></div>

    <h1 class="headline">
      <span class="verb line-1">reduce</span>
      <span class="object line-2">puffiness</span>
      <span class="amp">&amp;</span>
      <span class="verb line-3">improve</span>
      <span class="object line-4">overall</span>
      <span class="object line-5">look</span>
    </h1>

    <footer class="brand">
      <div class="brand-name">Odette Varga</div>
      <div class="brand-tagline">EUROPEAN SKIN CARE</div>
    </footer>
  </main>
</body>
</html>
```